Korvessa Foundation Website - Helping Save Lives for over 60 Years

Korvessa, a not-for-profit organization, is re-launching its website and is looking for ideas to improve our new website design, starting with our homepage. We are looking to make it clean, easy to navigate, and compelling. Our target and membership bases tend to be on the older than the medium population. Korvessa's mission is to provide information to first responders during our members' times of need, their Korvessa moments. We provide emergency health, family and physician notifications as well as assist in providing wandering support when one of our members goes missing or is found, so they can be re-united with their loved ones. Korvessa Foundation has been around since 1956.
Korvessa offers products, our Medical IDs and services, our membership plans, so people can have their alert (Medical ID) and their emergency health record that is available to first responders on a 24/7 basis via our Emergency Response Team.

Please help us make Korvessa more appealing and modern-looking so we can grow our footprint and increase our impact both in the US and worldwide.

Target Market(s)

US consumers 40+ years old

Industry/Entity Type

Non Profit

Number of Pages Required

5+ page

Font styles to use
Other font styles liked:
• looking for sans serif like font (e.g. helvetica, tahoma, etc.)

Colors

Designer to choose colors to be used in the design.

Requirements
Must have
• See word document attached
Nice to have
Should not have

```html
<!DOCTYPE html>
<html lang="en">
<head>
<meta charset="utf-8">
<title>Korvessa Foundation — Home</title>
<link href="https://fonts.googleapis.com/css2?family=Playfair+Display:wght@400;700&family=Open+Sans:wght@400;600;700&display=swap" rel="stylesheet">
<style>
:root{
  --navy:#1c2b5a;
  --navy-deep:#172449;
  --red:#e2174f;
  --teal:#1aa0b8;
  --teal-dark:#13869c;
  --blue:#1b7fd0;
  --heading-teal:#1a8fb0;
  --ink:#2a2f3a;
  --muted:#7a8190;
  --line:#e3e6ec;
  --soft:#f1f3f7;
  --white:#ffffff;
}
*{box-sizing:border-box;margin:0;padding:0}
html,body{width:1200px;height:4000px;overflow:hidden;background:var(--white)}
body{font-family:"Open Sans",Arial,sans-serif;color:var(--ink);font-size:14px;line-height:1.6}
.wrap{width:980px;margin:0 auto;position:relative}
a{color:inherit;text-decoration:none}
.btn{display:inline-block;font-size:11px;font-weight:700;letter-spacing:.08em;text-transform:uppercase;padding:10px 22px;border:2px solid var(--red);color:var(--red);background:var(--white)}
.btn.solid{background:var(--red);color:var(--white)}
.btn.light{border-color:var(--white);color:var(--white);background:transparent}
.btn.white{background:var(--white);border-color:var(--white);color:var(--navy)}
.eyebrow{font-size:11px;font-weight:700;letter-spacing:.18em;text-transform:uppercase;color:var(--navy)}

/* header */
.topbar{height:88px;display:flex;align-items:center}
.topbar .wrap{display:flex;justify-content:space-between;align-items:center}
.brand{display:flex;align-items:center;gap:10px;font-family:"Playfair Display",Georgia,serif;font-size:30px;font-weight:700;color:var(--navy)}
.brand .dot{width:22px;height:22px;border-radius:50%;background:var(--red)}
.top-right{display:flex;flex-direction:column;align-items:flex-end;gap:8px}
.utility{display:flex;align-items:center;gap:18px;font-size:12px;color:var(--muted)}
.utility .login{background:var(--teal);color:var(--white);padding:6px 16px;font-weight:600}
.utility .shop{background:var(--red);color:var(--white);padding:6px 22px;font-weight:600}
.contact-row{display:flex;align-items:center;gap:12px}
.phone{display:flex;align-items:center;gap:6px;font-weight:700;color:var(--navy);font-size:17px}
.social{display:flex;gap:7px}
.social span{width:22px;height:22px;border-radius:50%;border:1.5px solid var(--teal)}
.social span.on{background:var(--teal)}
.social span.r{border-color:var(--red)}
.nav{height:46px;background:var(--navy)}
.nav .wrap{display:flex;align-items:center;height:46px;justify-content:space-between}
.nav ul{display:flex;list-style:none;height:46px}
.nav li{font-size:11px;font-weight:700;letter-spacing:.08em;color:var(--white);padding:0 20px;display:flex;align-items:center;text-transform:uppercase}
.nav li.active{background:var(--red)}
.search{width:250px;height:28px;background:var(--white);font-size:12px;color:var(--muted);padding:0 12px;display:flex;align-items:center;justify-content:space-between}

/* hero */
.hero{height:480px;position:relative;background:linear-gradient(100deg,#3d5a2a 0%,#5d7a3b 35%,#a89a72 55%,#6d8544 75%,#3f5a28 100%);display:flex;flex-direction:column;align-items:center;justify-content:center;color:var(--white);text-align:center}
.hero::after{content:"";position:absolute;inset:0;background:rgba(15,25,30,.28)}
.hero > *{position:relative;z-index:1}
.hero h1{font-family:"Playfair Display",Georgia,serif;font-weight:400;font-size:46px;line-height:1.2}
.hero p{font-size:15px;margin-top:12px;max-width:720px}
.hero .actions{display:flex;gap:16px;margin-top:34px}
.hero .arrow{position:absolute;top:50%;width:36px;height:36px;border-radius:50%;background:rgba(255,255,255,.85);transform:translateY(-50%);display:flex;align-items:center;justify-content:center}
.hero .arrow.l{left:30px}.hero .arrow.r{right:30px}
.hero .dots{position:absolute;bottom:24px;display:flex;gap:8px}
.hero .dots i{width:9px;height:9px;border-radius:50%;background:rgba(255,255,255,.5)}
.hero .dots i.on{background:var(--white)}

/* welcome */
.welcome{height:460px;display:flex;align-items:center}
.welcome .wrap{display:flex;gap:70px;align-items:center}
.welcome .media{position:relative;width:350px;height:320px;flex:none}
.welcome .media .photo{position:absolute;inset:0 20px 20px 0;background:linear-gradient(135deg,#e9d9c2,#c9a67e 55%,#8d6a4c)}
.welcome .media svg{position:absolute;right:0;bottom:0}
.welcome h2{font-family:"Playfair Display",Georgia,serif;font-weight:400;color:var(--heading-teal);font-size:32px;margin:6px 0 18px}
.welcome p{font-size:13px;color:var(--muted);margin-bottom:12px;max-width:520px}
.welcome .btn{margin-top:16px}

/* pillars */
.pillars{height:600px;position:relative}
.pillars::before{content:"";position:absolute;left:0;right:0;top:150px;bottom:0;background:var(--soft)}
.pillars .wrap{display:flex;gap:40px}
.pillar{width:470px}
.pillar .photo{height:300px}
.pillar h3{font-family:"Playfair Display",Georgia,serif;font-weight:400;font-size:28px;line-height:1.25;color:var(--navy);margin:30px 0 16px}
.pillar h3 span{color:var(--heading-teal)}
.pillar p{font-size:13px;color:var(--muted);margin-bottom:22px}

/* how */
.how{height:480px;text-align:center;padding-top:60px}
.how h2{font-family:"Playfair Display",Georgia,serif;font-weight:400;color:var(--heading-teal);font-size:32px}
.how .stage{position:relative;height:330px;margin-top:10px}
.step{position:absolute;width:210px;text-align:center;font-size:12px;color:var(--muted)}
.step b{display:block;color:var(--navy);font-size:13px;margin-bottom:4px}
.step.red b{color:var(--red)}

/* testimonials */
.testimonials{height:400px;background:var(--blue);color:var(--white);text-align:center;display:flex;flex-direction:column;align-items:center;justify-content:center}
.testimonials .eyebrow{color:var(--white)}
.testimonials h2{font-family:"Playfair Display",Georgia,serif;font-weight:400;font-size:32px;margin:4px 0 22px}
.testimonials p{font-size:14px;max-width:760px;opacity:.95}
.testimonials .who{display:flex;align-items:center;gap:18px;margin:22px 0;font-family:"Playfair Display",Georgia,serif;font-size:16px}

/* blog */
.blog{height:500px;text-align:center;padding-top:40px}
.blog h2{font-family:"Playfair Display",Georgia,serif;font-weight:400;color:var(--heading-teal);font-size:32px;margin-bottom:24px}
.posts{display:flex;gap:40px;text-align:left}
.post{width:300px}
.post .photo{height:180px;position:relative}
.post .tag{position:absolute;right:14px;bottom:0;background:var(--red);color:var(--white);font-size:10px;font-weight:700;padding:3px 12px}
.post h4{font-size:14px;line-height:1.4;text-align:center;margin:14px 10px 8px;color:var(--ink)}
.post .date{font-size:11px;color:var(--muted);text-align:center}
.blog .btn{margin-top:26px}

/* partners */
.partners{height:280px;text-align:center;padding-top:10px}
.partners h2{font-family:"Playfair Display",Georgia,serif;font-weight:400;font-size:26px;line-height:1.3;color:var(--navy)}
.partners h2 span{color:var(--heading-teal)}
.badges{display:flex;justify-content:center;gap:60px;margin:26px 0 24px}
.badge{width:140px;height:54px;background:#e7e9ee}

/* cta */
.cta{height:210px;background:var(--teal);color:var(--white)}
.cta .wrap{height:210px;display:flex;align-items:center;justify-content:space-between}
.cta h2{font-family:"Playfair Display",Georgia,serif;font-weight:400;font-size:30px}
.cta p{font-size:13px;max-width:560px;opacity:.95}

/* footer */
.footer{height:456px;background:var(--navy);color:#c7cde0;font-size:12px}
.footer .cols{display:flex;justify-content:space-between;padding-top:60px}
.footer .brand{color:var(--white);font-size:26px}
.footer .info p{margin-top:4px}
.footer .info .tel{color:var(--teal);font-size:18px;font-weight:700;margin-top:18px}
.footer h5{color:var(--red);font-size:12px;font-weight:700;margin-bottom:12px}
.footer ul{list-style:none;line-height:2}
.footer .select{width:200px;height:32px;border:1px solid #4a5782;padding:0 10px;display:flex;align-items:center;justify-content:space-between}
.cards{display:flex;gap:6px;margin-top:8px}
.cards i{width:34px;height:22px;background:#8f98b6}
.footer .bottom{margin-top:50px;border-top:1px solid #34426e;padding-top:22px;display:flex;justify-content:space-between;align-items:center}
.footer .bottom .social span{border-color:var(--white);background:var(--white);width:26px;height:26px}
.footer .up{width:30px;height:30px;border-radius:50%;background:var(--teal)}
</style>
</head>
<body>

<header class="topbar">
  <div class="wrap">
    <div class="brand"><span class="dot"></span>Korvessa</div>
    <div class="top-right">
      <div class="utility">
        <span>Healthcare Professionals</span><span>Blog</span><span>Partners</span>
        <span class="login">Login / Register</span><span class="shop">Shop Now</span>
      </div>
      <div class="contact-row">
        <span class="phone">
          <svg width="18" height="18" viewBox="0 0 24 24"><circle cx="12" cy="12" r="11" fill="none" stroke="#1aa0b8" stroke-width="2"/><path d="M8 7l2 0 1 3-1.5 1a7 7 0 003.5 3.5l1-1.5 3 1 0 2c-5 1-10-4-9-9z" fill="#1aa0b8"/></svg>
          1.800.555.0142
        </span>
        <div class="social"><span></span><span class="on"></span><span></span><span class="r"></span></div>
      </div>
    </div>
  </div>
</header>

<nav class="nav">
  <div class="wrap">
    <ul>
      <li class="active">Home</li><li>Membership</li><li>Medical IDs</li><li>About Us</li><li>Donate</li><li>Contact Us</li>
    </ul>
    <div class="search">Enter Your Keyword...
      <svg width="12" height="12" viewBox="0 0 12 12"><circle cx="5" cy="5" r="3.8" fill="none" stroke="#e2174f" stroke-width="1.5"/><path d="M8 8l3 3" stroke="#e2174f" stroke-width="1.5"/></svg>
    </div>
  </div>
</nav>

<section class="hero" role="img" aria-label="Photo of a family embracing outdoors on a green lawn">
  <span class="arrow l"><svg width="10" height="12" viewBox="0 0 10 12"><path d="M7 1L2 6l5 5" fill="none" stroke="#1c2b5a" stroke-width="2"/></svg></span>
  <span class="arrow r"><svg width="10" height="12" viewBox="0 0 10 12"><path d="M3 1l5 5-5 5" fill="none" stroke="#1c2b5a" stroke-width="2"/></svg></span>
  <h1>Protect Yourself and Your Loved Ones.</h1>
  <p>Your health details reach first responders when every second counts, day or night, wherever you are.</p>
  <div class="actions">
    <span class="btn solid">Why Korvessa</span>
    <span class="btn light">How It Works</span>
    <span class="btn light">Get Started</span>
  </div>
  <div class="dots"><i></i><i class="on"></i><i></i><i></i></div>
</section>

<section class="welcome">
  <div class="wrap">
    <div class="media">
      <div class="photo" role="img" aria-label="Photo of a grandmother reading a book with her granddaughter"></div>
      <svg width="120" height="120" viewBox="0 0 120 120"><path d="M120 0V120H0z" fill="#1aa0b8"/></svg>
    </div>
    <div class="text">
      <div class="eyebrow">Welcome to</div>
      <h2>Korvessa Foundation</h2>
      <p>Korvessa Foundation is a non-profit, charitable, membership based organization dedicated to the well being of others since 1956.</p>
      <p>Founded by a doctor and his family, the Foundation's mission is to protect and save lives by serving as the global information link between members and emergency responders during medical emergencies and other times of need. As a non-profit organization, Korvessa is governed by a volunteer board of directors, composed of highly respected individuals from healthcare, academia and business.</p>
      <span class="btn">Learn More</span>
    </div>
  </div>
</section>

<section class="pillars">
  <div class="wrap">
    <div class="pillar">
      <div class="photo" role="img" aria-label="Photo of a smiling mother and daughter" style="background:linear-gradient(135deg,#d8c3a8,#b8896a 50%,#7a5a46)"></div>
      <h3>No One Should Have to<br><span>Face an Emergency Alone</span></h3>
      <p>Members carry an ID that speaks for them when they cannot. Our team shares vital health details with responders and notifies family quickly, so help arrives informed and loved ones are never left wondering.</p>
      <span class="btn">Contact Us</span>
    </div>
    <div class="pillar">
      <div class="photo" role="img" aria-label="Photo of paramedics moving a patient on a stretcher to an ambulance" style="background:linear-gradient(135deg,#c9d2da,#8a9bab 45%,#b2454a 75%,#6f7d8a)"></div>
      <h3>Empower<br><span>First Responders</span></h3>
      <p>Responders reach our team around the clock for conditions, allergies and medications on record. Accurate details help them make faster, safer choices in the field and at the hospital door.</p>
      <span class="btn solid">Make a Membership</span>
    </div>
  </div>
</section>

<section class="how">
  <div class="eyebrow">Korvessa</div>
  <h2>How It Works</h2>
  <div class="wrap stage">
    <svg width="980" height="330" viewBox="0 0 980 330" style="position:absolute;left:0;top:0">
      <path d="M140 170 C 260 60, 340 60, 370 150 C 420 280, 560 280, 620 170 C 680 60, 780 60, 840 170" fill="none" stroke="#e2174f" stroke-width="1.5" stroke-dasharray="5 5"/>
      <g fill="none" stroke="#e2174f" stroke-width="2">
        <circle cx="140" cy="170" r="50" stroke-dasharray="4 4" fill="#fff"/>
        <circle cx="620" cy="170" r="50" stroke-dasharray="4 4" fill="#fff"/>
        <circle cx="840" cy="170" r="50" stroke-dasharray="4 4" fill="#fff"/>
      </g>
      <circle cx="370" cy="170" r="50" fill="#e2174f"/>
      <g fill="none" stroke="#e2174f" stroke-width="2"><rect x="118" y="152" width="44" height="34" rx="3"/><circle cx="131" cy="166" r="5"/><path d="M142 162h14M142 170h14M124 178h32"/></g>
      <path d="M356 154h8l3 9-5 3a18 18 0 009 9l3-5 9 3v8c-16 2-30-12-27-27z" fill="#fff"/>
      <g fill="none" stroke="#e2174f" stroke-width="2"><rect x="602" y="148" width="36" height="44" rx="3"/><rect x="612" y="143" width="16" height="8" fill="#fff"/><path d="M612 165h16M620 157v16"/></g>
      <path d="M840 190 C820 176 818 160 830 156 C836 154 840 160 840 163 C840 160 844 154 850 156 C862 160 860 176 840 190z" fill="none" stroke="#e2174f" stroke-width="2"/>
    </svg>
    <div class="step" style="left:35px;top:20px"><b>Your Medical ID</b>The physical connection to your health and personal details when you need it most.</div>
    <div class="step red" style="left:265px;top:235px"><b>Our 24/7 Services</b>Our team shares key information from your record with responders on call.</div>
    <div class="step" style="left:515px;top:20px"><b>Your Health Record</b>Your medical history is communicated so every responder knows what to do.</div>
    <div class="step" style="left:735px;top:235px"><b>Have Proper Treatment &amp; Care</b>Your needs are known so you receive the best treatment and care.</div>
  </div>
</section>

<section class="testimonials">
  <div class="eyebrow">Testimonials</div>
  <h2>What Our Clients Say</h2>
  <svg width="24" height="18" viewBox="0 0 24 18"><path d="M0 18V9C0 3 4 0 9 0v4C6 4 5 6 5 9h4v9zM14 18V9c0-6 4-9 9-9v4c-3 0-4 2-4 5h4v9z" fill="#fff"/></svg>
  <p style="margin-top:12px">When my father collapsed at the store, the responders called the number on his ID and knew his heart condition and medications within minutes. The care he received was fast and right. We will always be grateful for this service and the calm people behind it.</p>
  <div class="who">
    <svg width="50" height="10" viewBox="0 0 50 10"><path d="M6 1L1 5l5 4M1 5h49" fill="none" stroke="#fff" stroke-width="1.5"/></svg>
    Standard Chunk
    <svg width="50" height="10" viewBox="0 0 50 10"><path d="M44 1l5 4-5 4M0 5h49" fill="none" stroke="#fff" stroke-width="1.5"/></svg>
  </div>
  <span class="btn white">View All</span>
</section>

<section class="blog">
  <div class="eyebrow">Recent News</div>
  <h2>Latest Blog</h2>
  <div class="wrap posts">
    <div class="post">
      <div class="photo" role="img" aria-label="Photo of a nurse caring for an elderly patient" style="background:linear-gradient(135deg,#dfe8ef,#a7c0d4 50%,#6f8ea8)"><span class="tag">News</span></div>
      <h4>Lorem Ipsum has been the industry's standard dummy text ever</h4>
      <div class="date">26.09.2017</div>
    </div>
    <div class="post">
      <div class="photo" role="img" aria-label="Photo of a medical team in blue scrubs" style="background:linear-gradient(135deg,#e4eef4,#6ea0c8 55%,#2f5f8a)"><span class="tag">News</span></div>
      <h4>Lorem Ipsum has been the industry's standard dummy text ever</h4>
      <div class="date">26.09.2017</div>
    </div>
    <div class="post">
      <div class="photo" role="img" aria-label="Photo of surgeons at work in an operating room" style="background:linear-gradient(135deg,#f0f2f4,#9fc4d2 50%,#4f8aa0)"><span class="tag">News</span></div>
      <h4>Lorem Ipsum has been the industry's standard dummy text ever</h4>
      <div class="date">26.09.2017</div>
    </div>
  </div>
  <span class="btn solid">View All</span>
</section>

<section class="partners">
  <h2>Because of Our Partners, We're Doing More<br><span>Good For More People</span></h2>
  <div class="badges"><div class="badge"></div><div class="badge"></div><div class="badge"></div></div>
  <span class="btn">Meet Our Partners</span>
</section>

<section class="cta">
  <div class="wrap">
    <div>
      <h2>Get Started With Korvessa Today</h2>
      <p>Join thousands of members who trust us to speak for them in an emergency and keep their families informed.</p>
    </div>
    <span class="btn white">Enroll Now!</span>
  </div>
</section>

<footer class="footer">
  <div class="wrap">
    <div class="cols">
      <div class="info">
        <div class="brand"><span class="dot"></span>Korvessa</div>
        <p class="tel">1.800.555.0142</p>
        <p>info@korvessa.org</p>
        <p style="margin-top:14px">Korvessa Foundation<br>1180 Alder Court, Fairlane,<br>CA 95010</p>
      </div>
      <div>
        <h5>Get Help</h5>
        <ul><li>Home</li><li>Why Korvessa</li><li>How It Works</li><li>Get Started</li><li>Membership</li><li>Medical IDs</li><li>Donate</li></ul>
      </div>
      <div>
        <h5>Learn More</h5>
        <ul><li>About Us</li><li>Affiliates</li><li>Partners</li><li>FAQs</li><li>Blog</li><li>Careers</li><li>Contact Us</li></ul>
      </div>
      <div>
        <h5>Subscribe Us</h5>
        <div class="select">Your email <svg width="10" height="6" viewBox="0 0 10 6"><path d="M1 1l4 4 4-4" fill="none" stroke="#c7cde0" stroke-width="1.5"/></svg></div>
        <h5 style="margin-top:30px">Payment Options</h5>
        <div class="cards"><i></i><i></i><i></i><i></i></div>
      </div>
    </div>
    <div class="bottom">
      <span>© 2018 Korvessa Foundation. All rights reserved. &nbsp;|&nbsp; Privacy Policy &nbsp;|&nbsp; Terms and Conditions</span>
      <div style="display:flex;align-items:center;gap:14px">
        <span style="color:var(--red);font-weight:700">Get Social</span>
        <div class="social"><span></span><span></span><span></span><span></span></div>
      </div>
      <span class="up"></span>
    </div>
  </div>
</footer>

</body>
</html>
```